Business Card for Professional Photographer

I'm looking for an eye catching modern clean design that compliments my logo/ website fonts & colours.
I specialise in architecture, corporate & commercial photography so I'm marketing to professional clients rather than portrait / wedding clients.

I would prefer to not have a solid black design.

My logo brand guide is as follows :

Main front font. : Reislust
Main font colour : #fff
Slogan front font : Ubuntu Bold
Monogram front font : Venti Medium
Container colour : #fff

I need print ready files in pdf .png & .eps formats.

Included in the files below are some screen grabs as reference to font & colours etc.

```html
<!DOCTYPE html>
<html lang="en">
<head>
<meta charset="utf-8">
<title>Clear Aperture – Business Card</title>
<link rel="stylesheet" href="https://fonts.googleapis.com/css2?family=Ubuntu:wght@400;500;700&display=swap">
<style>
  :root {
    --canvas: #e6e6e6;
    --card: #ffffff;
    --gold: #b8862b;
    --ink: #1f1f1f;
    --muted: #6b6b6b;
    --shadow: rgba(0, 0, 0, 0.16);
  }
  * { box-sizing: border-box; margin: 0; padding: 0; }
  html, body {
    width: 1200px;
    height: 1021px;
    overflow: hidden;
    background: var(--canvas);
    font-family: "Ubuntu", sans-serif;
  }
  .sheet {
    width: 1200px;
    height: 1021px;
    display: flex;
    flex-direction: column;
    align-items: center;
    justify-content: center;
    gap: 44px;
  }
  .card {
    position: relative;
    width: 760px;
    height: 434px;
    background: var(--card);
    box-shadow: 0 6px 18px var(--shadow);
  }

  /* Company name and slogan */
  .brand {
    display: flex;
    flex-direction: column;
  }
  .brand-name {
    color: var(--gold);
    font-weight: 400;
    white-space: nowrap;
    line-height: 1.1;
  }
  .brand-slogan {
    color: var(--muted);
    font-weight: 400;
    white-space: nowrap;
  }

  /* Front */
  .card-front .brand {
    position: absolute;
    left: 50%;
    top: 50%;
    transform: translate(-50%, -50%);
    align-items: center;
  }
  .card-front .brand-name { font-size: 42px; }
  .card-front .brand-slogan { font-size: 15px; margin-top: 10px; }

  /* Back */
  .card-back .brand {
    position: absolute;
    left: 52px;
    top: 46px;
  }
  .card-back .brand-name { font-size: 34px; }
  .card-back .brand-slogan { font-size: 13px; margin-top: 8px; }

  .contact {
    position: absolute;
    left: 150px;
    top: 150px;
    color: var(--ink);
    font-size: 19px;
    line-height: 1.3;
  }
  .person-name {
    color: var(--gold);
    font-weight: 700;
    font-size: 24px;
    letter-spacing: 0.02em;
  }
  .person-role { margin-bottom: 22px; }
  .address { margin-bottom: 6px; }
  .contact-list { list-style: none; }
  .contact-list li {
    display: flex;
    align-items: center;
    gap: 10px;
  }
  .contact-icon {
    width: 16px;
    height: 16px;
    flex: none;
    fill: none;
    stroke: var(--gold);
    stroke-width: 1.8;
  }
  .contact-icon .solid { fill: var(--gold); stroke: none; }
</style>
</head>
<body>
<main class="sheet">

  <section class="card card-front">
    <div class="brand">
      <span class="brand-name">Clear Aperture</span>
      <span class="brand-slogan">Buildings, Business &amp; Brands</span>
    </div>
  </section>

  <section class="card card-back">
    <div class="brand">
      <span class="brand-name">Clear Aperture</span>
      <span class="brand-slogan">Buildings, Business &amp; Brands</span>
    </div>

    <div class="contact">
      <p class="person-name">Daniel Hartley</p>
      <p class="person-role">Photographer</p>
      <p class="address">48 Norwood Lane<br>Kelvin Grove QLD 4059</p>
      <ul class="contact-list">
        <li>
          <svg class="contact-icon" viewBox="0 0 16 16" aria-hidden="true">
            <path class="solid" d="M3.2 1.2l2.4 0 1 3.4-1.6 1.2c.8 1.8 2.2 3.2 4 4l1.2-1.6 3.4 1v2.4c0 1-1 2-2 2C6.4 13.6 2.4 9.6 1.2 4.6c0-1.4 1-3.4 2-3.4z"/>
          </svg>
          <span>(07) 3210-5487</span>
        </li>
        <li>
          <svg class="contact-icon" viewBox="0 0 16 16" aria-hidden="true">
            <rect x="1.5" y="3.5" width="13" height="9"/>
            <path d="M1.5 3.5l6.5 5 6.5-5"/>
          </svg>
          <span>daniel@clearaperture.com</span>
        </li>
        <li>
          <svg class="contact-icon" viewBox="0 0 16 16" aria-hidden="true">
            <circle cx="8" cy="8" r="6.5"/>
            <ellipse cx="8" cy="8" rx="3" ry="6.5"/>
            <path d="M1.5 8h13M2.5 4.8h11M2.5 11.2h11"/>
          </svg>
          <span>www.clearaperture.com</span>
        </li>
      </ul>
    </div>
  </section>

</main>
</body>
</html>
```